Christmas and New Years time

We need to design a custom Facebook Cover Page for El Taller de Brisaluna, with focus on Celebration themes, featuring Christmas and New Year's time

El Taller de Brisaluna is specialized on customized wedding invitations, from idea to design and print.

Pagoramo.com/eltallerdebrisaluna

In case you need more information please let us know.

Bruno

```html
<!DOCTYPE html>
<html lang="es">
<head>
<meta charset="utf-8">
<title>El Taller de Brisaluna — Algo para celebrar</title>
<link rel="stylesheet" href="https://fonts.googleapis.com/css2?family=Noto+Serif+Display:wdth,wght@75,700&family=Open+Sans:wght@400&display=swap">
<style>
  :root {
    --plum-deep: #3f1429;
    --plum: #5a1d3c;
    --magenta-glow: #9a2a6a;
    --ribbon: #c8136e;
    --badge-white: #ffffff;
    --badge-line: #ddd2d8;
    --ink: #4a1a30;
    --ornament-pink: #d4257c;
    --ornament-plum: #6b3a52;
    --edge: #b86a92;
  }
  html, body {
    margin: 0;
    padding: 0;
    overflow: hidden;
    background: var(--plum-deep);
  }
  .cover {
    position: relative;
    width: 1200px;
    height: 444px;
    overflow: hidden;
    background: radial-gradient(ellipse 460px 300px at 622px 222px, var(--magenta-glow) 0%, var(--plum) 55%, var(--plum-deep) 100%);
  }
  .cover-art {
    position: absolute;
    inset: 0;
  }
  .badge-title {
    font-family: "Noto Serif Display", Georgia, serif;
    font-stretch: 75%;
    font-weight: 700;
    fill: var(--ink);
  }
  .badge-title--top { font-size: 45px; }
  .badge-title--main { font-size: 74px; }
  .contact {
    position: absolute;
    right: 34px;
    top: 190px;
    margin: 0;
    text-align: right;
    font-family: "Open Sans", Arial, sans-serif;
    font-size: 17px;
    line-height: 25px;
    color: var(--badge-white);
  }
</style>
</head>
<body>
<main class="cover">
  <svg class="cover-art" width="1200" height="444" viewBox="0 0 1200 444">
    <line class="edge-line" x1="6" y1="0" x2="6" y2="444" stroke="var(--edge)" stroke-width="1.5" stroke-dasharray="4 4"/>
    <line class="edge-line" x1="1194" y1="0" x2="1194" y2="444" stroke="var(--edge)" stroke-width="1.5" stroke-dasharray="4 4"/>

    <rect class="ribbon" x="0" y="166" width="1200" height="112" fill="var(--ribbon)"/>
    <line class="ribbon-stitch" x1="0" y1="177" x2="1200" y2="177" stroke="var(--badge-white)" stroke-width="2"/>
    <line class="ribbon-stitch" x1="0" y1="267" x2="1200" y2="267" stroke="var(--badge-white)" stroke-width="2"/>

    <circle class="badge-shadow" cx="626" cy="228" r="210" fill="#000" opacity="0.22"/>
    <circle class="badge-scallop" cx="622" cy="222" r="204" fill="none" stroke="var(--badge-white)" stroke-width="12" stroke-linecap="round" stroke-dasharray="0 14.24"/>
    <circle class="badge" cx="622" cy="222" r="204" fill="var(--badge-white)"/>
    <circle class="badge-ring" cx="622" cy="222" r="192" fill="none" stroke="var(--badge-line)" stroke-width="1.5"/>

    <rect class="trees" x="562" y="58" width="92" height="62" rx="6" fill="var(--ornament-pink)" opacity="0.85" role="img" aria-label="Three small Christmas trees with a star"/>
    <rect class="flourish" x="512" y="140" width="220" height="24" rx="12" fill="var(--ornament-plum)" opacity="0.7" role="img" aria-label="Decorative scroll flourish"/>
    <rect class="flourish" x="512" y="278" width="220" height="24" rx="12" fill="var(--ornament-plum)" opacity="0.7" role="img" aria-label="Decorative scroll flourish"/>
    <rect class="fireworks" x="542" y="328" width="140" height="52" rx="8" fill="var(--ornament-pink)" opacity="0.85" role="img" aria-label="Three New Year fireworks bursts"/>

    <text class="badge-title badge-title--top" x="622" y="209" text-anchor="middle" textLength="256" lengthAdjust="spacingAndGlyphs">ALGO PARA</text>
    <text class="badge-title badge-title--main" x="622" y="268" text-anchor="middle" textLength="274" lengthAdjust="spacingAndGlyphs">CELEBRAR</text>
  </svg>

  <p class="contact">+595 21 480917<br>www.brisaluna.com.py</p>
</main>
</body>
</html>
```